Business cards to launch an education platform

Hi,
I am looking at having new business cards designed.
I am a startup, developing a web platform for schools and university, the education world. It's an online assessment system.
I would like a card that looks classy, and that is using the colors and the font of my logo.

I have attached:
1) my logo
2) A business card that I have designed quickly so you can have all the information required in the card, but I really don't like it.
3) The font that I am using (Lato Regular) to design my web platform
4) Some screenshots of my web platform so you can have a look at the style that I have.

Target Market(s)

Major market: Education system: Schools and university
Minor markets: Business in general

Industry/Entity Type

Business

Contact Information for Business Card

Lydia Marsh
Director

M: 0437 681 902
E: lydia.marsh@copperLeafSystems.com.au

Requirements
Must have
• The colors of my logo

```html
<!DOCTYPE html>
<html lang="en">
<head>
<meta charset="utf-8">
<title>Copper Leaf Systems — Business Card</title>
<link href="https://fonts.googleapis.com/css2?family=Lato:wght@300;400;700&display=swap" rel="stylesheet">
<style>
  :root {
    --backdrop: #e6e8ea;
    --card: #ffffff;
    --card-shade: #eef0f2;
    --brand-blue: #1b7fc4;
    --brand-sky: #2fb0ea;
    --band-deep: #1f86d1;
    --ink: #2e3338;
    --ink-soft: #7a8087;
  }
  * { box-sizing: border-box; margin: 0; padding: 0; }
  html, body { width: 1200px; height: 912px; overflow: hidden; }
  body {
    background: var(--backdrop);
    font-family: "Lato", sans-serif;
    color: var(--ink);
    display: flex;
    align-items: center;
    justify-content: center;
    gap: 44px;
  }
  .card {
    position: relative;
    width: 540px;
    height: 309px;
    border-radius: 22px;
    background: linear-gradient(160deg, var(--card) 55%, var(--card-shade));
    box-shadow: 0 6px 18px rgba(0,0,0,0.12);
    overflow: hidden;
  }
  .brand {
    display: flex;
    align-items: center;
    gap: 12px;
  }
  .brand-square {
    width: 46px;
    height: 46px;
    background: var(--brand-blue);
    border-radius: 4px;
    flex: none;
  }
  .brand-name {
    font-weight: 400;
    color: var(--brand-blue);
    font-size: 30px;
    letter-spacing: 1.5px;
    line-height: 1;
    text-transform: uppercase;
  }
  .card-front .brand {
    position: absolute;
    left: 50%;
    top: 50%;
    transform: translate(-50%, -50%);
  }
  .card-back .brand {
    position: absolute;
    left: 36px;
    bottom: 58px;
    gap: 8px;
  }
  .card-back .brand-square { width: 28px; height: 28px; }
  .card-back .brand-name { font-size: 17px; letter-spacing: 1px; }
  .contact {
    position: absolute;
    right: 44px;
    top: 40px;
    width: 300px;
  }
  .contact-name {
    font-weight: 700;
    font-size: 19px;
    letter-spacing: 1px;
    text-transform: uppercase;
  }
  .contact-role {
    font-size: 9px;
    letter-spacing: 1.5px;
    color: var(--ink-soft);
    text-transform: uppercase;
    margin: 2px 0 10px;
  }
  .contact-list { list-style: none; }
  .contact-list li {
    display: flex;
    align-items: center;
    gap: 8px;
    font-size: 12.5px;
    line-height: 21px;
  }
  .contact-list svg { width: 12px; height: 12px; flex: none; fill: var(--ink); }
  .band {
    position: absolute;
    left: 0; right: 0; bottom: 0;
    height: 26px;
    background: linear-gradient(180deg, var(--brand-sky), var(--band-deep));
  }
  .band::before {
    content: "";
    position: absolute;
    left: 0; right: 0; top: -5px;
    height: 5px;
    background: #9fdcf6;
  }
</style>
</head>
<body>
  <section class="card card-front" aria-label="Card front">
    <div class="brand">
      <span class="brand-square"></span>
      <span class="brand-name">Copper Leaf Systems</span>
    </div>
  </section>

  <section class="card card-back" aria-label="Card back">
    <div class="contact">
      <p class="contact-name">Lydia Marsh</p>
      <p class="contact-role">Director</p>
      <ul class="contact-list">
        <li><svg viewBox="0 0 16 16"><path d="M3.6 1.2l2.3 2.6-1.3 1.6c.9 2 2.4 3.5 4.4 4.4l1.6-1.3 2.6 2.3-1.2 2.3C7 14.6 1.4 9 1.3 2.4z"/></svg>0437 681 902</li>
        <li><svg viewBox="0 0 16 16"><path d="M4 1h8v14H4zM5.5 2.5v9h5v-9zM7 12.5h2v1.2H7z"/></svg>0437 681 902</li>
        <li><svg viewBox="0 0 16 16"><path d="M1 3h14v10H1zM2.5 4.5v.4L8 8.6l5.5-3.7v-.4zM2.5 6.7v4.8h11V6.7L8 10.4z"/></svg>lydia.marsh@copperLeafSystems.com.au</li>
        <li><svg viewBox="0 0 16 16"><path d="M8 1a7 7 0 100 14A7 7 0 008 1zm0 1.5c.8 0 1.7 1.4 2 3.5H6c.3-2.1 1.2-3.5 2-3.5zM2.6 7.2h2.2v1.6H2.6zm3.4 0h4v1.6H6zm5.2 0h2.2v1.6h-2.2zM6 10h4c-.3 2.1-1.2 3.5-2 3.5S6.3 12.1 6 10z"/></svg>www.copperLeafSystems.com.au</li>
        <li><svg viewBox="0 0 16 16"><path d="M8 1a5 5 0 00-5 5c0 3.7 5 9 5 9s5-5.3 5-9a5 5 0 00-5-5zm0 7a2 2 0 110-4 2 2 0 010 4z"/></svg>14 Elmstead Road, Level 3, Carlton</li>
      </ul>
    </div>
    <div class="brand">
      <span class="brand-square"></span>
      <span class="brand-name">Copper Leaf Systems</span>
    </div>
    <div class="band"></div>
  </section>
</body>
</html>
```